Mahu Suds (Modern, Upscale, Organic Coffee Soap Packaging)

We need a new packaging design for a Hawaii-based, organic soap company called "Mahu Suds" ('Mahu' means 'Coffee' in the Hawaiian Language). Our eco-conscious mission is to 'upcycle' brewed coffee grounds from local coffee shops and cafes and transform them into high-quality soap and scrub products.For greater reference, please check out our main marketing platform - Instagram (@mahusuds).We currently package our soaps in recycled paper envelopes (as demonstrated on our Instagram page and the attached file). While our customers really enjoy modern yet rustic aesthetic of the paper envelope, our issue is that consumers can't see or really smell the soaps without removing them from the packaging.

Target Market(s)

Millenials, People from Hawaii, People from Japan (one of Hawaii's biggest tourist markets)

Industry/Entity Type

Beauty

Font styles to use
Sans Serif

Colors

Designer to choose only greyscale colors for use in the design.

Requirements
Must have
• - must include/incorporate our original logo
• - must keep with aesthetic displayed on our website and instagram
Nice to have
• - I would like to see something that really communicates our commitment to our social mission to help the environment
• - I would like to see elegant, minimalist design (white marble?)
• - A soap packaging that would feel at home in a modern luxury home (bauhaus?)
Should not have
• - should not have any colors other than white, black, or gray (possibly coffee brown okay)

```html
<!DOCTYPE html>
<html lang="en">
<head>
<meta charset="utf-8">
<title>Mahu Suds – Plumeria Label</title>
<link rel="stylesheet" href="https://fonts.googleapis.com/css2?family=Montserrat:wght@600&family=Raleway:wght@300;700&family=Roboto+Condensed:wght@300;700&display=swap">
<style>
  :root {
    --ink: #111111;
    --ink-soft: #333333;
    --paper: #fbfbfb;
    --rule: #444444;
  }
  * { margin: 0; padding: 0; box-sizing: border-box; }
  html, body { width: 1200px; height: 1200px; overflow: hidden; background: var(--paper); }
  .label {
    position: relative;
    width: 1200px;
    height: 1200px;
    background: var(--paper);
    color: var(--ink);
    text-align: center;
  }
  .label > * { position: absolute; left: 0; width: 100%; }
  .brand-name {
    top: 188px;
    font-family: "Montserrat", sans-serif;
    font-weight: 600;
    font-size: 176px;
    line-height: 1;
    letter-spacing: 0.2em;
    padding-left: 0.2em;
  }
  .brand-sub {
    top: 388px;
    font-family: "Roboto Condensed", sans-serif;
    font-weight: 300;
    font-size: 58px;
    letter-spacing: 0.12em;
    line-height: 1;
  }
  .definition {
    top: 470px;
    font-family: "Raleway", sans-serif;
    font-weight: 300;
    font-size: 38px;
    line-height: 1;
    color: var(--ink-soft);
  }
  .scent {
    top: 622px;
    font-family: "Raleway", sans-serif;
    font-weight: 700;
    font-size: 36px;
    line-height: 1;
    color: var(--ink-soft);
  }
  .contact {
    top: 792px;
    font-family: "Raleway", sans-serif;
    font-weight: 300;
    font-size: 27px;
    line-height: 33px;
    color: var(--ink-soft);
  }
  .origin {
    top: 964px;
    font-family: "Raleway", sans-serif;
    font-weight: 300;
    font-size: 39px;
    line-height: 1;
    color: var(--ink-soft);
  }
  .claims {
    top: 1033px;
    left: 277px;
    width: 644px;
    height: 95px;
    display: flex;
    border-left: 2px solid var(--rule);
  }
  .claim {
    flex: 1;
    border-right: 2px solid var(--rule);
    display: flex;
    flex-direction: column;
    justify-content: center;
    align-items: center;
    font-family: "Roboto Condensed", sans-serif;
    font-weight: 700;
    color: var(--ink);
    text-transform: uppercase;
    line-height: 1.05;
  }
  .claim-main { font-size: 21px; }
  .claim-small { font-size: 16px; }
</style>
</head>
<body>
  <main class="label">
    <h1 class="brand-name">MAHU</h1>
    <p class="brand-sub">SOAP CO.</p>
    <p class="definition">ma*hu /ma-hu/ n. Coffee, coffee beans</p>
    <p class="scent">Scent: Plumeria</p>
    <p class="contact">@mahusuds<br>www.mahusuds.com</p>
    <p class="origin">Hand made in Hawaii</p>
    <ul class="claims">
      <li class="claim"><span class="claim-main">100%</span><span class="claim-main">Vegan</span></li>
      <li class="claim"><span class="claim-main">Locally</span><span class="claim-main">Sourced</span></li>
      <li class="claim"><span class="claim-main">Hand</span><span class="claim-small">Crafted</span></li>
      <li class="claim"><span class="claim-main">Uncycled</span><span class="claim-small">Coffe Grounds</span></li>
    </ul>
  </main>
</body>
</html>
```